KBRF website design

We need a page template website design for a cms website. Please see the brief attached for the details.
The client is the Kestrel Brook Ramfold Federation which is an organisation promoting the White Suffolk Sheep Breed within Australia.
Updates

Reason: So that my top few designs can make changes and re-submit.

Target Market(s)

See attached brief

```html
<!DOCTYPE html>
<html lang="en">
<head>
<meta charset="utf-8">
<title>Kestrel Brook Ramfold Federation</title>
<link href="https://fonts.googleapis.com/css2?family=PT+Sans:ital,wght@0,400;0,700;1,400&family=Arimo:ital,wght@0,400;0,700;1,400&display=swap" rel="stylesheet">
<style>
:root{
  --green:#135f3e;
  --green-dark:#0f5234;
  --red:#c0212b;
  --yellow:#f4c52b;
  --grey-dark:#3d3d3d;
  --footer:#262626;
  --page:#eeeeee;
  --text:#3f3f3f;
  --muted:#a8a8a8;
}
*{margin:0;padding:0;box-sizing:border-box}
html,body{width:1124px;height:1200px;overflow:hidden;background:var(--page);font-family:"Arimo",Arial,sans-serif;color:var(--text)}
.page{position:relative;width:1124px;height:1200px}
.header{position:absolute;left:0;top:0;width:1124px;height:107px;background:#fff}
.brand{position:absolute;left:145px;top:24px;display:flex;align-items:center;gap:12px}
.brand-mark{width:60px;height:60px;border-radius:50%;background:var(--yellow);border:3px solid var(--green)}
.brand-name{font-family:"PT Sans",sans-serif;font-weight:700;font-size:33px;color:var(--green);letter-spacing:.5px;white-space:nowrap}
.tagline{position:absolute;left:728px;top:68px;font-family:"PT Sans",sans-serif;font-style:italic;font-size:17px;color:var(--red)}
.nav{position:absolute;left:0;top:107px;width:1124px;height:40px;background:linear-gradient(#555,#333)}
.nav a{position:absolute;top:7px;height:27px;line-height:27px;font-size:11px;font-weight:700;color:#fff;text-decoration:none;text-align:center}
.nav a.active{background:var(--green)}
.hero{position:absolute;left:0;top:147px;width:1124px;height:390px}
.content-shadow{position:absolute;left:300px;top:538px;width:660px;height:8px;background:radial-gradient(ellipse at top,rgba(0,0,0,.14),transparent 70%)}
.intro{position:absolute;left:147px;top:581px;width:608px}
.intro h2,.sponsors h2,.card h3{font-family:"PT Sans",sans-serif;font-weight:700;color:var(--text)}
.intro h2{font-size:18px;margin-bottom:13px}
.intro p{font-size:11.2px;line-height:15.6px;text-align:justify;margin-bottom:15.6px}
.sponsors{position:absolute;left:809px;top:574px}
.sponsors h2{font-size:17px;margin-bottom:11px}
.sponsor-box{width:185px;height:142px;border:6px solid var(--yellow);background:#fff;position:relative}
.divider{position:absolute;left:132px;top:782px;width:859px;border-top:1px dotted #b5b5b5}
.card{position:absolute;top:817px;height:92px;background:linear-gradient(#fff,#f1f1f1);border:2px solid #fff;border-radius:6px;box-shadow:0 7px 6px -5px rgba(0,0,0,.18)}
.card h3{position:absolute;left:14px;top:9px;font-size:16px}
.card svg{position:absolute;left:16px;top:38px}
.card .lead{position:absolute;left:62px;top:43px;font-size:14px;color:#555;white-space:nowrap}
.card .more{position:absolute;left:62px;top:61px;font-size:9px;font-style:italic;color:#444}
.footer{position:absolute;left:0;top:999px;width:1124px;height:201px;background:var(--footer)}
.questions{position:absolute;left:0;top:986px;width:1124px;text-align:center;font-family:"PT Sans",sans-serif;font-size:21px;color:#fff}
.foot-links{position:absolute;left:0;top:1074px;width:1124px;text-align:center;font-size:10px;color:var(--muted)}
.foot-links span{margin:0 6px}
.social{position:absolute;left:477px;top:1113px;width:170px;height:22px;border:1px solid #8fa0c8;border-radius:2px;background:linear-gradient(#6179b3,#3d5697);display:flex;align-items:center}
.social .sq{width:20px;height:20px;background:#2d4680;margin-left:1px}
.social span{font-family:"PT Sans",sans-serif;font-weight:700;font-size:12.5px;color:#fff;margin-left:8px}
.copy{position:absolute;left:0;top:1156px;width:1124px;text-align:center;font-size:10.5px;line-height:16.5px;color:var(--muted)}
</style>
</head>
<body>
<div class="page">
  <header class="header">
    <div class="brand"><div class="brand-mark"></div><div class="brand-name">Kestrel Brook Ramfold Federation</div></div>
    <div class="tagline">...Better by Design</div>
  </header>

  <nav class="nav">
    <a class="active" style="left:134px;width:71px">HOME</a>
    <a style="left:250px;width:62px">ABOUT</a>
    <a style="left:370px;width:68px">SEARCH</a>
    <a style="left:510px;width:92px">STUD PAGES</a>
    <a style="left:663px;width:60px">SALES</a>
    <a style="left:778px;width:62px">LINKS</a>
    <a style="left:914px;width:70px">CONTACT</a>
  </nav>

  <svg class="hero" width="1124" height="390" viewBox="0 0 1124 390">
    <defs>
      <linearGradient id="field" x1="0" y1="0" x2="0" y2="1">
        <stop offset="0" stop-color="#c9d8ea"/>
        <stop offset=".35" stop-color="#5d7a4a"/>
        <stop offset=".6" stop-color="#6fa347"/>
        <stop offset="1" stop-color="#5ea13a"/>
      </linearGradient>
    </defs>
    <rect width="1124" height="390" fill="var(--green)"/>
    <polygon points="0,303 130,316 562,348 994,316 1124,303 1124,390 0,390" fill="var(--grey-dark)"/>
    <polygon points="130,316 562,342 994,316 994,318 562,372 130,318" fill="var(--green)"/>
    <polygon points="130,316 480,326 562,372 644,326 994,316 562,348" fill="var(--green)"/>
    <polygon role="img" aria-label="Flock of white sheep grazing on a green paddock below forested hills" points="130,0 994,0 994,316 562,348 130,316" fill="url(#field)"/>
    <circle cx="539" cy="352" r="5" fill="#fff"/>
    <circle cx="556" cy="352" r="5" fill="#444"/>
    <circle cx="574" cy="352" r="5" fill="#444"/>
    <circle cx="592" cy="352" r="5" fill="#444"/>
  </svg>
  <div class="content-shadow"></div>

  <section class="intro">
    <h2>Why Chosse Us</h2>
    <p><b>Lorem ipsum dolor sit amet, consectetuer adipiscing elit. Nam cursus. Morbi ut mi. Nullam enim leo, egestas id, condimentum at, laoreet mattis, massa.</b> Sed eleifend nonummy diam. Praesent mauris ante, elementum et, bibendum at, posuere sit amet, nibh. Duis tincidunt lectus quis dui viverra vestibulum. Suspendisse vulputate aliquam dui. Nulla elementum dui ut augue. Aliquam vehicula mi at mauris. Maecenas placerat, nisl at consequat rhoncus, sem nunc gravida justo, quis eleifend arcu velit quis lacus.</p>
    <p>Pellentesque habitant morbi tristique senectus et netus et malesuada fames ac turpis egestas. In posuere felis nec tortor. Pellentesque faucibus. Ut accumsan ultricies elit...</p>
  </section>

  <aside class="sponsors">
    <h2>Sponsors</h2>
    <div class="sponsor-box">
      <svg width="173" height="130" viewBox="0 0 173 130">
        <rect x="62" y="30" width="44" height="36" rx="8" fill="#2c5fa8"/>
        <rect x="8" y="76" width="82" height="26" rx="4" fill="#c9a227"/>
        <circle cx="146" cy="84" r="20" fill="#7bbf2a"/>
      </svg>
    </div>
  </aside>

  <div class="divider"></div>

  <div class="card" style="left:134px;width:203px">
    <h3>Prime Lamb Helpline</h3>
    <svg width="32" height="32" viewBox="0 0 32 32"><circle cx="16" cy="15" r="12" fill="none" stroke="var(--green)" stroke-width="2.5"/><circle cx="12" cy="14" r="1.6" fill="var(--green)"/><circle cx="20" cy="14" r="1.6" fill="var(--green)"/></svg>
    <div class="lead">Lorem Ipsum dolor.</div><div class="more">read more</div>
  </div>
  <div class="card" style="left:355px;width:203px">
    <h3>Events</h3>
    <svg width="30" height="30" viewBox="0 0 30 30"><rect x="3" y="5" width="24" height="22" fill="none" stroke="var(--green)" stroke-width="2.5"/><rect x="3" y="5" width="24" height="5" fill="var(--green)"/><path d="M8 14h14M8 18h14M8 22h14M11 12v13M15 12v13M19 12v13" stroke="var(--green)" stroke-width="1.5"/></svg>
    <div class="lead">Lorem Ipsum dolor.</div><div class="more">read more</div>
  </div>
  <div class="card" style="left:574px;width:197px;height:89px">
    <h3>Members</h3>
    <svg width="30" height="32" viewBox="0 0 30 32"><circle cx="12" cy="8" r="6" fill="var(--green)"/><path d="M2 30c0-10 4-14 10-14s10 4 10 14z" fill="var(--green)"/><circle cx="22" cy="24" r="6" fill="#fff" stroke="var(--green)" stroke-width="2"/><path d="M22 20v8M18 24h8" stroke="var(--green)" stroke-width="2"/></svg>
    <div class="lead" style="top:41px">Lorem Ipsum dolor.</div><div class="more" style="top:59px">read more</div>
  </div>
  <div class="card" style="left:790px;top:815px;width:203px;height:92px">
    <h3>Latest News</h3>
    <svg width="30" height="28" viewBox="0 0 30 28"><rect x="2" y="4" width="26" height="20" fill="none" stroke="var(--green)" stroke-width="2.5"/><rect x="6" y="9" width="8" height="7" fill="var(--green)"/><path d="M17 10h8M17 14h8M6 19h19" stroke="var(--green)" stroke-width="2"/></svg>
    <div class="lead">Lorem Ipsum dolor.</div><div class="more">read more</div>
  </div>

  <footer class="footer"></footer>
  <svg style="position:absolute;left:0;top:964px" width="1124" height="82" viewBox="0 0 1124 82">
    <polygon points="421,0 690,0 684,35 1075,35 562,81 40,35 428,35" fill="var(--green)"/>
    <rect x="0" y="34" width="40" height="1.5" fill="var(--red)"/>
  </svg>
  <div class="questions">Questions?&nbsp; 08 7400 3190</div>

  <div class="foot-links">Home<span>|</span>About Us<span>|</span>Members<span>|</span>Stud Pages<span>|</span>News<span>|</span>Sales<span>|</span>Link<span>|</span>Contact</div>
  <div class="social"><div class="sq"></div><span>Connect with Flockline</span></div>
  <div class="copy">Copyright © 2014 Kestrel Brook Ramfold Federation. All rights reserved.<br>Website design and development by Fernhook Studio</div>
</div>
</body>
</html>
```